ebook cover for a womens core fitness business

I need an ebook cover for an email capture gift. The title is "Ways to iron-clad your lower stability". My website provides online workouts for women focussing on their core and pelvic floor muscles. My business is "Lumen Motion with Tia" I have attached my color scheme as well as logo file

Target Market(s)

Females from child bearing age onwards

Industry/Entity Type

Health And Wellness

Font styles to use
Sans Serif

Colors
33a6d7
0455a3
cee9f5

Requirements
Must have
• Colours as per file.
• Feel fresh and attractive to women but not flowery
• Look professional
Should not have
• Flowers

```html
<!DOCTYPE html>
<html lang="en">
<head>
<meta charset="UTF-8">
<title>Lumen Motion with Tia – Ebook Cover</title>
<link rel="stylesheet" href="https://fonts.googleapis.com/css2?family=Barlow:wght@300;400;600;700&display=swap">
<style>
  :root {
    --backdrop: #e6e8ea;
    --paper: #ffffff;
    --brand-navy: #0455a3;
    --brand-sky: #33a6d7;
    --brand-mist: #cee9f5;
    --ink: #1c2433;
    --photo-sky: #eef3f4;
    --photo-teal: #1f6f86;
    --photo-teal-deep: #165a6d;
    --photo-green: #5f7a52;
    --photo-stand: #d9dde0;
  }
  * { margin: 0; padding: 0; box-sizing: border-box; }
  html, body {
    width: 1200px;
    height: 801px;
    overflow: hidden;
    background: var(--backdrop);
  }
  .canvas {
    position: relative;
    width: 1200px;
    height: 801px;
  }
  .cover {
    position: absolute;
    left: 370px;
    top: 74px;
    width: 461px;
    height: 652px;
    background: var(--paper);
    overflow: hidden;
    font-family: "Barlow", Arial, sans-serif;
  }
  .cover-photo {
    position: absolute;
    left: 150px;
    top: 0;
    width: 311px;
    height: 652px;
    background:
      linear-gradient(90deg, var(--paper) 0%, rgba(255,255,255,0.85) 18%, rgba(255,255,255,0) 45%),
      radial-gradient(ellipse 38% 42% at 62% 48%, var(--photo-teal) 0%, var(--photo-teal-deep) 55%, rgba(22,90,109,0) 100%),
      radial-gradient(ellipse 30% 20% at 40% 35%, var(--photo-green) 0%, rgba(95,122,82,0) 100%),
      radial-gradient(ellipse 35% 18% at 95% 40%, var(--photo-green) 0%, rgba(95,122,82,0) 100%),
      linear-gradient(180deg, var(--photo-sky) 0%, var(--photo-sky) 40%, var(--photo-stand) 70%, #c9cfd3 100%);
  }
  .brand {
    position: absolute;
    left: 36px;
    top: 34px;
    display: flex;
    align-items: center;
    gap: 8px;
  }
  .brand-dot {
    width: 10px;
    height: 10px;
    border-radius: 50%;
    background: var(--brand-sky);
  }
  .brand-name {
    font-size: 21px;
    font-weight: 600;
    color: var(--brand-navy);
    letter-spacing: 0.2px;
  }
  .brand-rule {
    position: absolute;
    left: 36px;
    top: 68px;
    width: 146px;
    height: 1px;
    background: var(--brand-sky);
  }
  .title {
    position: absolute;
    left: 36px;
    top: 444px;
    text-transform: uppercase;
    line-height: 1;
  }
  .title span { display: block; }
  .title-light {
    font-size: 31px;
    font-weight: 300;
    color: var(--ink);
    letter-spacing: 0.5px;
  }
  .title-accent {
    margin-top: 9px;
    font-size: 34px;
    font-weight: 700;
    color: var(--brand-navy);
  }
  .title-light + .title-light { margin-top: 0; }
  .title-accent + .title-light { margin-top: 12px; }
  .title-strong {
    margin-top: 8px;
    font-size: 34px;
    font-weight: 700;
    color: var(--ink);
  }
</style>
</head>
<body>
  <div class="canvas">
    <article class="cover">
      <div class="cover-photo" role="img" aria-label="Photo of a woman in teal leggings and running shoes stepping up stadium stairs outdoors"></div>
      <div class="brand">
        <span class="brand-dot"></span>
        <span class="brand-name">Lumen Motion with Tia</span>
      </div>
      <div class="brand-rule"></div>
      <h1 class="title">
        <span class="title-light">Ways to</span>
        <span class="title-accent">Iron-clad</span>
        <span class="title-light">Your lower</span>
        <span class="title-strong">Stability</span>
      </h1>
    </article>
  </div>
</body>
</html>
```